Corvanta Energy LNG as Marine Fuel Powerpoint Design

Powerpoint template inspired by and using the attached Corvanta Energy logo. We are developing LNG as marine fuel facilities and bunkering vessels to supply the fuel to the marine industry. Designs should use the Corvanta Energy logo colors and be consistent with our vision of providing environmentally cleaner fuel supply. Our selected logo was 1A in the attached files, as shown on the business card template also attached.

Target Market(s)

Marine Industry (Shipping, container vessels, crude carriers, cargo / transportation vessels, etc.)

Requirements
Must have
• Clean / green energy theme
Compatibility with submitted logo and logo color scheme
Font headers that work well with the logo font
Nice to have
• Marine / Maritime theme
relevance to Gulf Coast Region
Should not have
• Dark colors

```html
<!DOCTYPE html>
<html lang="en">
<head>
<meta charset="utf-8">
<title>Corvanta Energy – LNG as Marine Fuel Presentation</title>
<link rel="stylesheet" href="https://fonts.googleapis.com/css2?family=Audiowide&family=Source+Sans+3:wght@400;600;700&display=swap">
<style>
  :root {
    --board: #f6f6f6;
    --slide-edge: #c9c9c9;
    --ink: #1f2428;
    --title: #37474f;
    --muted: #8a8a8a;
    --accent-line: #d9553f;
    --brand-blue: #1a6fae;
    --deep-blue: #0a3f86;
    --sky-blue: #1b8ec4;
    --band-pale: #e6eef6;
    --series-a: #5b9bd5;
    --series-b: #333f4f;
    --series-c: #1fc3f5;
    --grid: #dcdcdc;
  }
  * { box-sizing: border-box; margin: 0; padding: 0; }
  html, body { width: 1200px; height: 740px; overflow: hidden; background: var(--board); }
  body { position: relative; font-family: "Source Sans 3", Arial, sans-serif; color: var(--ink); }

  .slide-frame { position: absolute; width: 381px; height: 215px; }
  .slide {
    position: absolute; left: 0; top: 0; width: 425px; height: 240px;
    transform: scale(0.8965); transform-origin: 0 0;
    background: #fff; border: 1px solid var(--slide-edge); overflow: hidden;
  }
  .slide > * { position: absolute; }
  .slide-number { position: absolute; font-size: 11px; color: var(--muted); }
  .sorter-cursor { position: absolute; left: 399px; top: 500px; width: 2px; height: 228px; background: var(--accent-line); }

  .header-band { left: 0; top: 0; width: 425px; height: 88px; background: linear-gradient(90deg, var(--sky-blue), var(--deep-blue)); }
  .footer-band { left: 0; top: 176px; width: 425px; height: 64px; background: var(--band-pale); }

  .cover-title { font-family: "Audiowide", sans-serif; color: var(--title); font-size: 17px; letter-spacing: .5px; text-transform: uppercase; line-height: 1.05; }
  .section-title { font-family: "Audiowide", sans-serif; color: var(--title); font-size: 13px; letter-spacing: .4px; text-transform: uppercase; line-height: 1.15; }
  .subtitle { font-size: 8px; }
  .cover-date { font-size: 8px; }
  .cover-date strong { font-weight: 700; }
  .slide-date { left: 15px; top: 13px; font-size: 3.6px; font-weight: 600; }

  .brand { display: flex; align-items: center; gap: 3px; font-weight: 700; color: var(--brand-blue); white-space: nowrap; }
  .brand-dot { border-radius: 50%; background: var(--brand-blue); flex: none; }
  .brand--large { font-size: 8.5px; }
  .brand--large .brand-dot { width: 10px; height: 10px; }
  .brand--small { font-size: 4.6px; gap: 2px; }
  .brand--small .brand-dot { width: 6px; height: 6px; }

  .fine-print { font-size: 5.9px; line-height: 1.4; text-decoration: underline; }
  .body-copy { font-size: 9px; line-height: 1.4; }

  .agenda-heading { font-size: 9.5px; font-weight: 700; }
  .bullet-list { list-style: none; font-size: 7.5px; }
  .bullet-list li { margin-bottom: 9px; display: flex; align-items: center; gap: 6px; }
  .bullet-list li::before { content: ""; width: 4px; height: 1.2px; background: var(--ink); }
</style>
</head>
<body>

<!-- Slide 1: cover -->
<div class="slide-frame" style="left:11px;top:7px">
  <section class="slide">
    <div class="header-band" role="img" aria-label="Decorative blue header band"></div>
    <h1 class="cover-title" style="left:22px;top:108px">What is Lorem Ipsum?</h1>
    <p class="subtitle" style="left:22px;top:148px">What is Lorem Ipsum?</p>
    <p class="cover-date" style="left:22px;top:198px"><strong>Date:</strong> July 22, 2020</p>
    <div class="brand brand--large" style="left:338px;top:198px"><span class="brand-dot"></span>Corvanta Energy</div>
  </section>
</div>
<span class="slide-number" style="left:12px;top:232px">1</span>

<!-- Slide 2: title -->
<div class="slide-frame" style="left:410px;top:7px">
  <section class="slide">
    <div class="header-band" role="img" aria-label="Decorative blue header band"></div>
    <h1 class="cover-title" style="left:22px;top:108px;width:220px">What is Lorem Ipsum?</h1>
    <p class="subtitle" style="left:22px;top:158px">What is Lorem Ipsum?</p>
    <div class="brand brand--large" style="left:338px;top:210px"><span class="brand-dot"></span>Corvanta Energy</div>
  </section>
</div>
<span class="slide-number" style="left:411px;top:232px">2</span>

<!-- Slide 3: text -->
<div class="slide-frame" style="left:810px;top:7px">
  <section class="slide">
    <div class="footer-band" role="img" aria-label="Decorative pale blue footer band"></div>
    <p class="slide-date">July 22, 2020</p>
    <div class="brand brand--small" style="left:360px;top:28px"><span class="brand-dot"></span>Corvanta Energy</div>
    <h2 class="cover-title" style="left:15px;top:43px">What is Lorem Ipsum?</h2>
    <div class="fine-print" style="left:15px;top:70px;width:392px">
      <p>Lorem Ipsum is simply dummy text of the printing and typesetting industry. Lorem Ipsum has been the industry's standard dummy text ever since the 1500s, when an unknown printer took a galley of type and scrambled it to make a type specimen book. It has survived not only five centuries, but also the leap into electronic typesetting, remaining essentially unchanged. Lorem Ipsum is simply dummy text of the printing and typesetting industry. Lorem Ipsum has been the industry's standard dummy text ever since the 1500s, when an unknown printer took a galley of type and scrambled it to make a type specimen book. It has survived not only five centuries, but also the leap into electronic typesetting, remaining essentially unchanged.</p>
      <p style="margin-top:7px">Lorem Ipsum is simply dummy text of the printing and typesetting industry. Lorem Ipsum has been the industry's standard dummy text ever since the 1500s, when an unknown printer took a galley of type and scrambled it to make a type specimen book. It has survived not only five centuries, but also the leap into electronic typesetting, remaining essentially unchanged.</p>
    </div>
  </section>
</div>
<span class="slide-number" style="left:811px;top:232px">3</span>

<!-- Slide 4: two text columns -->
<div class="slide-frame" style="left:11px;top:256px">
  <section class="slide">
    <div class="footer-band" role="img" aria-label="Decorative pale blue footer band"></div>
    <p class="slide-date">July 22, 2020</p>
    <div class="brand brand--small" style="left:360px;top:24px"><span class="brand-dot"></span>Corvanta Energy</div>
    <p class="fine-print" style="left:15px;top:57px;width:135px">Lorem Ipsum is simply dummy text of the printing and typesetting industry. Lorem Ipsum has been the industry's standard dummy text ever since the 1500s, when an unknown printer took a galley of type and scrambled it to make a type specimen book.</p>
    <p class="body-copy" style="left:211px;top:56px;width:195px">Lorem Ipsum is simply dummy text of the printing and typesetting industry. Lorem Ipsum has been the industry's standard dummy text ever since the 1500s, when an unknown printer took a galley of type and scrambled it to make a type specimen book. It has survived not only five centuries, but also the leap into electronic typesetting, remaining essentially unchanged.</p>
    <h2 class="section-title" style="left:211px;top:203px;width:170px">What is Lorem Ipsum?</h2>
  </section>
</div>
<span class="slide-number" style="left:12px;top:481px">4</span>

<!-- Slide 5: text with photo -->
<div class="slide-frame" style="left:410px;top:256px">
  <section class="slide">
    <div class="footer-band" role="img" aria-label="Decorative pale blue footer band"></div>
    <p class="slide-date">July 22, 2020</p>
    <div class="brand brand--small" style="left:360px;top:24px"><span class="brand-dot"></span>Corvanta Energy</div>
    <p class="body-copy" style="left:15px;top:57px;width:182px">Lorem Ipsum is simply dummy text of the printing and typesetting industry. Lorem Ipsum has been the industry's standard dummy text ever since the 1500s, when an unknown printer took a galley of type and scrambled it to make a type specimen book.</p>
    <div role="img" aria-label="Photo of an engineer and a child in a hard hat reviewing plans at a bright office desk" style="left:212px;top:55px;width:192px;height:140px;background:linear-gradient(120deg,#dfe9f2 0%,#6f9fc6 45%,#e8ecef 100%)"></div>
    <h2 class="section-title" style="left:212px;top:203px;width:170px">What is Lorem Ipsum?</h2>
  </section>
</div>
<span class="slide-number" style="left:411px;top:481px">5</span>

<!-- Slide 6: photo pair -->
<div class="slide-frame" style="left:810px;top:256px">
  <section class="slide">
    <div class="footer-band" role="img" aria-label="Decorative pale blue footer band"></div>
    <p class="slide-date">July 22, 2020</p>
    <div class="brand brand--small" style="left:360px;top:24px"><span class="brand-dot"></span>Corvanta Energy</div>
    <div role="img" aria-label="Photo of a hiker with an orange backpack in a sunlit autumn forest" style="left:16px;top:55px;width:195px;height:140px;background:linear-gradient(135deg,#d9c7a4 0%,#b58a4e 45%,#6b5a3a 100%)"></div>
    <div role="img" aria-label="Photo of a potted flowering plant beside a weathered wooden post" style="left:212px;top:55px;width:192px;height:140px;background:linear-gradient(110deg,#7a6a55 0%,#a89a80 40%,#6f8a56 75%,#c9c3b6 100%)"></div>
  </section>
</div>
<span class="slide-number" style="left:811px;top:481px">6</span>

<!-- Slide 7: bullets with chart -->
<div class="slide-frame" style="left:11px;top:505px">
  <section class="slide">
    <div class="footer-band" role="img" aria-label="Decorative pale blue footer band"></div>
    <p class="slide-date">July 22, 2020</p>
    <div class="brand brand--small" style="left:360px;top:24px"><span class="brand-dot"></span>Corvanta Energy</div>
    <h3 class="agenda-heading" style="left:15px;top:57px">What is Lorem Ipsum?</h3>
    <ul class="bullet-list" style="left:15px;top:90px">
      <li>Bullets 1</li>
      <li>Bullets 2</li>
      <li>Bullets 3</li>
    </ul>
    <svg style="left:0;top:0;width:425px;height:240px" viewBox="0 0 425 240" role="img" aria-label="Clustered bar chart of three series across four categories">
      <g stroke="var(--grid)" stroke-width=".6">
        <line x1="220" x2="402" y1="58" y2="58"/><line x1="220" x2="402" y1="77" y2="77"/>
        <line x1="220" x2="402" y1="96" y2="96"/><line x1="220" x2="402" y1="115" y2="115"/>
        <line x1="220" x2="402" y1="134" y2="134"/><line x1="220" x2="402" y1="153" y2="153"/>
        <line x1="220" x2="402" y1="172" y2="172"/>
      </g>
      <g font-size="3.5" fill="#aaa" font-family="Source Sans 3, sans-serif" text-anchor="end">
        <text x="217" y="59">6</text><text x="217" y="78">5</text><text x="217" y="97">4</text>
        <text x="217" y="116">3</text><text x="217" y="135">2</text><text x="217" y="154">1</text><text x="217" y="173">0</text>
      </g>
      <g fill="var(--series-a)">
        <rect x="226" y="90" width="10" height="82"/><rect x="271" y="124" width="10" height="48"/>
        <rect x="316" y="106" width="10" height="66"/><rect x="361" y="86" width="10" height="86"/>
      </g>
      <g fill="var(--series-b)">
        <rect x="237" y="126" width="10" height="46"/><rect x="282" y="88" width="10" height="84"/>
        <rect x="327" y="138" width="10" height="34"/><rect x="372" y="119" width="10" height="53"/>
      </g>
      <g fill="var(--series-c)">
        <rect x="248" y="134" width="10" height="38"/><rect x="293" y="134" width="10" height="38"/>
        <rect x="338" y="115" width="10" height="57"/><rect x="383" y="79" width="10" height="93"/>
      </g>
      <g font-size="3.6" fill="#b5b5b5" font-family="Source Sans 3, sans-serif" text-anchor="middle">
        <text x="242" y="179">Category 1</text><text x="287" y="179">Category 2</text>
        <text x="332" y="179">Category 3</text><text x="377" y="179">Category 4</text>
      </g>
      <g font-size="3.4" fill="#b5b5b5" font-family="Source Sans 3, sans-serif">
        <rect x="270" y="185" width="3" height="3" fill="var(--series-a)"/><text x="275" y="188">Series 1</text>
        <rect x="298" y="185" width="3" height="3" fill="var(--series-b)"/><text x="303" y="188">Series 2</text>
        <rect x="326" y="185" width="3" height="3" fill="var(--series-c)"/><text x="331" y="188">Series 3</text>
      </g>
    </svg>
    <h2 class="section-title" style="left:230px;top:203px;width:170px;text-align:center">What is Lorem Ipsum?</h2>
  </section>
</div>
<span class="slide-number" style="left:12px;top:730px">7</span>

<div class="sorter-cursor"></div>

</body>
</html>
```